Business Card for Jewelry Business

We need a new namecard design for a jewelry company based in Bangkok, Thailand. We have a new website recently and want the new namecard to reflect our new modern image. I have uploaded our old namecard to show you the information that needs to be on the namecard. Pls check our website www.qelburn.com for the new color scheme to help design the new namecard.

```html
<!DOCTYPE html>
<html lang="en">
<head>
<meta charset="utf-8">
<title>Qelburn Manufacturers – Business Card</title>
<link rel="stylesheet" href="https://fonts.googleapis.com/css2?family=Libre+Baskerville:wght@400;700&display=swap">
<style>
  :root {
    --backdrop: #3b3c3f;
    --teal: #55c4c8;
    --white: #ffffff;
    --ink: #222425;
    --card-radius: 14px;
  }
  * { box-sizing: border-box; margin: 0; padding: 0; }
  html, body {
    width: 1200px; height: 801px; overflow: hidden;
    background: var(--backdrop);
    font-family: "Libre Baskerville", Georgia, serif;
  }
  .stage {
    position: relative; width: 1200px; height: 801px;
    display: flex; align-items: center; justify-content: center; gap: 40px;
  }
  .card {
    position: relative; width: 540px; height: 309px;
    border-radius: var(--card-radius);
    box-shadow: 0 14px 30px rgba(0,0,0,0.45);
    overflow: hidden;
  }
  /* Front */
  .card--front { background: var(--teal); }
  .brand {
    position: absolute; left: 0; right: 0; top: 50%;
    transform: translateY(-50%);
    text-align: center; color: var(--white); font-weight: 400;
  }
  .brand__name { font-size: 40px; letter-spacing: 3px; line-height: 1.1; }
  .brand__sub { font-size: 11px; letter-spacing: 3px; margin-top: 8px; }

  /* Back */
  .card--back { background: var(--white); border-bottom: 4px solid var(--teal); }
  .person { position: absolute; left: 38px; top: 52px; width: 300px; }
  .person__name {
    color: var(--teal); font-weight: 700; font-size: 25px; letter-spacing: 1px;
  }
  .person__role {
    color: var(--ink); font-size: 10.5px; letter-spacing: 0.5px; margin-top: 4px;
    padding-bottom: 8px; border-bottom: 2px solid var(--teal);
  }
  .contacts { position: absolute; left: 38px; top: 150px; list-style: none; }
  .contact {
    display: flex; align-items: center; gap: 14px; margin-bottom: 12px;
    color: var(--ink); font-size: 11.5px; line-height: 1.45;
  }
  .contact__icon {
    flex: none; width: 30px; height: 30px; border-radius: 50%;
    background: var(--teal); display: flex; align-items: center; justify-content: center;
  }
  .back-brand {
    position: absolute; right: 40px; top: 62px;
    color: var(--teal); font-size: 22px; letter-spacing: 2px; font-weight: 400;
  }
</style>
</head>
<body>
<main class="stage">
  <section class="card card--front" aria-label="Card front">
    <div class="brand">
      <div class="brand__name">QELBURN</div>
      <div class="brand__sub">MANUFACTURERS</div>
    </div>
  </section>

  <section class="card card--back" aria-label="Card back">
    <div class="back-brand">QELBURN</div>
    <div class="person">
      <h1 class="person__name">NIRA SATCHAPAN</h1>
      <p class="person__role">SALES &amp; PRODUCT DEVELOPMENT MANAGER</p>
    </div>
    <ul class="contacts">
      <li class="contact">
        <span class="contact__icon">
          <svg width="16" height="16" viewBox="0 0 24 24" aria-hidden="true"><path fill="#fff" d="M6.6 10.8a15 15 0 0 0 6.6 6.6l2.2-2.2a1 1 0 0 1 1-.25 11.4 11.4 0 0 0 3.6.6 1 1 0 0 1 1 1V20a1 1 0 0 1-1 1A17 17 0 0 1 3 4a1 1 0 0 1 1-1h3.5a1 1 0 0 1 1 1c0 1.25.2 2.45.6 3.6a1 1 0 0 1-.25 1z"/></svg>
        </span>
        <span>+662-418-2203<br>+662-584-3190 (Fax)</span>
      </li>
      <li class="contact">
        <span class="contact__icon">
          <svg width="16" height="16" viewBox="0 0 24 24" aria-hidden="true"><g fill="none" stroke="#fff" stroke-width="2"><circle cx="12" cy="12" r="9"/><path d="M3 12h18M12 3c3 3 3 15 0 18M12 3c-3 3-3 15 0 18"/></g></svg>
        </span>
        <span>nira@qelburn.com<br>www.qelburn.com</span>
      </li>
      <li class="contact">
        <span class="contact__icon">
          <svg width="16" height="16" viewBox="0 0 24 24" aria-hidden="true"><path fill="#fff" d="M12 2a7 7 0 0 0-7 7c0 5 7 13 7 13s7-8 7-13a7 7 0 0 0-7-7zm0 9.5A2.5 2.5 0 1 1 12 6.5a2.5 2.5 0 0 1 0 5z"/></svg>
        </span>
        <span>128 Moo 7 Suanthong Road,<br>Pha Rim Industrial Estate,<br>Bangkok, 10580 Thailand</span>
      </li>
    </ul>
  </section>
</main>
</body>
</html>
```